Design of a carbonated cola drink

our competitor is selling brindle cola
their design is en closed
we need a similar design colours but we cant use
brindle cola
we were thinking of usuing
the words KVO cola
using a bit of the american flag colors red and blue
designs for three flavors shown below should be shown
the main drink colour is zapp red
orange bluma orange
punch like wintzel /zolvin burst

Target Market(s)

pacific islands

Requirements
Must have
• mentioned above
Nice to have
• mentioned above

```html
<!DOCTYPE html>
<html lang="en">
<head>
<meta charset="utf-8">
<title>KVO Soda Labels</title>
<link rel="stylesheet" href="https://fonts.googleapis.com/css2?family=Alfa+Slab+One&family=Montserrat:wght@800&family=Pinyon+Script&display=swap">
<style>
  :root {
    --backdrop: #000000;
    --ink-white: #ffffff;
    --punch-body: #2a8a0a;
    --punch-band: #1d5400;
    --punch-dots: #7cfc00;
    --cola-body: #ff0a0c;
    --cola-band: #9a0000;
    --cola-dots: #7a0000;
    --orange-body: #ff3d00;
    --orange-band: #ff0000;
    --orange-dots: #ffa51f;
  }
  * { margin: 0; padding: 0; box-sizing: border-box; }
  html, body {
    width: 1200px;
    height: 854px;
    overflow: hidden;
    background: var(--backdrop);
  }
  .label-sheet {
    position: relative;
    width: 1200px;
    height: 854px;
  }
  .label {
    position: absolute;
    top: 32px;
    width: 346px;
    height: 790px;
    background: var(--body);
    overflow: hidden;
  }
  .label--punch  { left: 34px;  --body: var(--punch-body);  --band: var(--punch-band);  --dots: var(--punch-dots); }
  .label--cola   { left: 418px; --body: var(--cola-body);   --band: var(--cola-band);   --dots: var(--cola-dots); }
  .label--orange { left: 814px; --body: var(--orange-body); --band: var(--orange-band); --dots: var(--orange-dots); }

  .label__band {
    height: 40px;
    background: var(--band);
    color: var(--ink-white);
    font-family: "Montserrat", sans-serif;
    font-weight: 800;
    font-size: 26px;
    line-height: 42px;
    text-align: center;
    letter-spacing: 0.5px;
  }
  .label__texture {
    position: absolute;
    left: 0;
    top: 40px;
    width: 100%;
    height: 432px;
    background: linear-gradient(to bottom, var(--dots) 0%, color-mix(in srgb, var(--dots) 55%, transparent) 45%, transparent 100%);
    opacity: 0.85;
  }
  .label__brand,
  .label__flavour {
    position: absolute;
    writing-mode: vertical-rl;
    transform: rotate(180deg);
    color: var(--ink-white);
    white-space: nowrap;
  }
  .label__brand {
    left: 88px;
    top: 84px;
    width: 112px;
    height: 572px;
    font-family: "Alfa Slab One", serif;
    font-size: 150px;
    line-height: 112px;
    text-align: center;
    letter-spacing: 34px;
  }
  .label__flavour {
    left: 212px;
    width: 110px;
    font-family: "Pinyon Script", cursive;
    font-size: 104px;
    line-height: 110px;
    text-align: left;
  }
  .label--punch  .label__flavour { top: 160px; height: 292px; }
  .label--cola   .label__flavour { top: 236px; height: 216px; }
  .label--orange .label__flavour { top: 200px; height: 252px; }
</style>
</head>
<body>
<main class="label-sheet">
  <section class="label label--punch">
    <h2 class="label__band">KVO PUNCH</h2>
    <div class="label__texture" role="img" aria-label="Halftone dot pattern in light green, fading downward"></div>
    <p class="label__brand">KVO</p>
    <p class="label__flavour">Punch</p>
  </section>
  <section class="label label--cola">
    <h2 class="label__band">KVO COLA</h2>
    <div class="label__texture" role="img" aria-label="Halftone dot pattern in dark red, fading downward"></div>
    <p class="label__brand">KVO</p>
    <p class="label__flavour">Cola</p>
  </section>
  <section class="label label--orange">
    <h2 class="label__band">KVO ORANGE</h2>
    <div class="label__texture" role="img" aria-label="Halftone dot pattern in light orange, fading downward"></div>
    <p class="label__brand">KVO</p>
    <p class="label__flavour">Orange</p>
  </section>
</main>
</body>
</html>
```